Flirt Wed or Ditch Show Flyer 2017

We are 3 female comedians who need to brand a new show that we want to take on the road. The show will be geared towards relationships. We will perform at clubs and theaters. We will also end up needing a logo etc for tee shirts and business cards and website. Etc. I am including some photos of the 3 of us from an old flyer from another show we did together ... it's not 'great' but it shows the 3 of us. ... perhaps there would be room for headshots also? or maybe we would add one shot of the 3 of us? There's also a chance we might want to include a 'guest' once in a while. The flyer should include space for the venue details and time date etc. and website. www.flirtwedorditch.example

Target Market(s)

Women. PG 13 and up. but not boxed in for just women. guys will have HUGE FUN TOO.

Logo Text

'Flirt Wed or Ditch'

Font styles to use
Sans Serif

Colors
e667a6
f04a50

Requirements
Must have
• Flirt Wed or Ditch
• possible tag lines- '3 comedians looking for love and finding the funny' or 'love means never having to say you're funny' or '3 funny women with choices'
• (we are still ironing out exactly the lines)
• names of 3 comedians: Nina Castell, Dorothy Vance, Tessa Wilbrook
• space to easily edit venue name - date - time
Should not have
• no swirly bits. it should look strong and powerful but feminine.

```html
<!DOCTYPE html>
<html lang="en">
<head>
<meta charset="utf-8">
<title>Flirt Wed or Ditch – Show Flyer</title>
<link rel="stylesheet" href="https://fonts.googleapis.com/css2?family=Bebas+Neue&family=Fredoka:wght@600&family=Lora:wght@400&display=swap">
<style>
  :root {
    --pink: #e667a6;
    --pink-deep: #c94f8c;
    --pink-bright: #ff6fb8;
    --coral: #f04a50;
    --ribbon-tail: #a9524f;
    --white: #ffffff;
    --page: #ffffff;
  }
  * { box-sizing: border-box; margin: 0; padding: 0; }
  html, body { width: 1000px; height: 1200px; overflow: hidden; background: var(--page); }
  .canvas { position: relative; width: 1000px; height: 1200px; background: var(--page); }
  .flyer {
    position: absolute; left: 116px; top: 45px; width: 779px; height: 1070px;
    background: var(--pink); overflow: hidden; color: var(--white);
  }
  .corner-pattern { position: absolute; top: 0; width: 165px; height: 118px; }
  .corner-pattern--left { left: 0; }
  .corner-pattern--right { right: 0; }
  .bottom-pattern {
    position: absolute; left: 0; bottom: 0; width: 100%; height: 175px;
    background: linear-gradient(180deg, var(--pink) 0%, var(--pink-bright) 35%, var(--pink-deep) 100%);
  }
  .show-title {
    position: absolute; left: 0; right: 0; top: 140px; text-align: center;
    font-family: "Fredoka", sans-serif; font-weight: 600; font-size: 76px; line-height: 1.02;
    color: var(--white);
  }
  .tagline {
    position: absolute; left: 0; right: 0; top: 293px; text-align: center;
    font-family: "Lora", serif; font-size: 22px; color: var(--white);
  }
  .tagline .num { font-size: 30px; }
  .rule {
    position: absolute; left: 47px; right: 48px; height: 4px;
    border-top: 1px solid var(--white); background: var(--coral);
  }
  .rule--top { top: 344px; }
  .rule--bottom { top: 449px; }
  .show-date {
    position: absolute; left: 0; right: 0; top: 363px; text-align: center;
    font-family: "Bebas Neue", sans-serif; font-size: 45px; letter-spacing: 1px; line-height: 1;
  }
  .show-venue {
    position: absolute; left: 0; right: 0; top: 410px; text-align: center;
    font-family: "Bebas Neue", sans-serif; font-size: 29px; letter-spacing: 1px; line-height: 1;
  }
  .cast-photo {
    position: absolute; left: 58px; top: 492px; width: 652px; height: 283px;
    border-radius: 120px 120px 0 0;
    background: linear-gradient(180deg, #e9b3cf 0%, #b77a9c 45%, #4a2a3c 100%);
  }
  .name-banner { position: absolute; left: 19px; top: 770px; width: 736px; height: 105px; }
  .name-banner svg { position: absolute; inset: 0; }
  .cast-list {
    position: absolute; left: 30px; top: 3px; width: 675px; height: 99px;
    display: flex; list-style: none;
  }
  .cast-member {
    flex: 1; display: flex; flex-direction: column; align-items: center; justify-content: center;
    font-family: "Fredoka", sans-serif; font-weight: 600; color: var(--white); line-height: 1.05;
  }
  .cast-member .first { font-size: 23px; }
  .cast-member .last { font-size: 34px; }
</style>
</head>
<body>
<div class="canvas">
  <main class="flyer">
    <svg class="corner-pattern corner-pattern--left" viewBox="0 0 165 118" role="img" aria-label="Pink checkered corner pattern">
      <defs>
        <linearGradient id="cornerFade" x1="0" y1="0" x2="1" y2="1">
          <stop offset="0" stop-color="#ff6fb8"/>
          <stop offset="1" stop-color="#c94f8c"/>
        </linearGradient>
      </defs>
      <polygon points="0,0 165,0 0,118" fill="url(#cornerFade)"/>
    </svg>
    <svg class="corner-pattern corner-pattern--right" viewBox="0 0 165 118" role="img" aria-label="Pink checkered corner pattern">
      <defs>
        <linearGradient id="cornerFadeR" x1="1" y1="0" x2="0" y2="1">
          <stop offset="0" stop-color="#ff6fb8"/>
          <stop offset="1" stop-color="#c94f8c"/>
        </linearGradient>
      </defs>
      <polygon points="0,0 165,0 165,118" fill="url(#cornerFadeR)"/>
    </svg>

    <h1 class="show-title">Flirt Wed<br>or Ditch</h1>
    <p class="tagline"><span class="num">3</span> Comedians looking for love &amp; finding the funny</p>

    <div class="rule rule--top"></div>
    <p class="show-date">Saturday, December 17, 2016 at 9PM</p>
    <p class="show-venue">Boston, 8th Avenue, Civic Lantern Hall</p>
    <div class="rule rule--bottom"></div>

    <div class="cast-photo" role="img" aria-label="Group photo of the three comedians side by side"></div>

    <div class="name-banner">
      <svg viewBox="0 0 736 105" aria-hidden="true">
        <polygon points="0,30 30,30 30,90 12,90" fill="var(--ribbon-tail)"/>
        <polygon points="736,30 706,30 706,90 724,90" fill="var(--ribbon-tail)"/>
        <rect x="31.5" y="1.5" width="673" height="101" fill="var(--coral)" stroke="var(--white)" stroke-width="3"/>
        <line x1="266" y1="10" x2="266" y2="95" stroke="var(--white)" stroke-width="3" stroke-dasharray="14 8"/>
        <line x1="468" y1="10" x2="468" y2="95" stroke="var(--white)" stroke-width="3" stroke-dasharray="14 8"/>
      </svg>
      <ul class="cast-list">
        <li class="cast-member"><span class="first">Nina</span><span class="last">Castell</span></li>
        <li class="cast-member"><span class="first">Dorothy</span><span class="last">Vance</span></li>
        <li class="cast-member"><span class="first">Tessa</span><span class="last">Wilbrook</span></li>
      </ul>
    </div>

    <div class="bottom-pattern" role="img" aria-label="Pink checkered woven band pattern"></div>
  </main>
</div>
</body>
</html>
```